Keepsakes & Novelties: Promotional Products and Apparel- Tri fold hand out

Promotional Products / Advertising Specialties distributor with in-house manufacturing capabilities. We want to improve our Tri-Fold hand out that we use for Tradeshows and new customers.
Our old Tri-fold is attached. I don't care for the layout and much of the content, so I would use it as an example of how not to do the new tri-fold. Our business card is attached and I'd like the color scheme of the new tri-fold to match the color scheme of the business card. Our logo is attached and a word doc is attached for the content / text of the new tri-fold. Tri-fold should use a combination of pictures and text. Front cover should clearly define Promotional Products and Corporate Apparel.

Target Market(s)

Corporate Business

Industry/Entity Type

Advertising

Colors
3176b5

Requirements
Must have
• company name, phone, address, web
Nice to have
• Pics of screen printing, embroidery equipment
Should not have
• n/a

```html
<!DOCTYPE html>
<html lang="en">
<head>
<meta charset="utf-8">
<title>Keepsakes &amp; Novelties Tri-Fold</title>
<link href="https://fonts.googleapis.com/css2?family=Lilita+One&family=Open+Sans:ital,wght@0,400;0,600;0,700;1,600&family=Noto+Serif:wght@700&display=swap" rel="stylesheet">
<style>
:root{
  --brand-blue:#3176b5;
  --deep-blue:#1f5d9c;
  --panel-grey:#e9eaeb;
  --ink:#1c1c1c;
  --accent-orange:#f7b244;
  --white:#ffffff;
  --stage:#2b1630;
}
*{box-sizing:border-box;margin:0;padding:0}
html,body{width:1200px;height:900px;overflow:hidden}
body{background:radial-gradient(circle at 60% 40%,#3b2140,var(--stage));font-family:"Open Sans",sans-serif;position:relative}
.spread{position:absolute;left:290px;width:620px;height:436px;display:grid;grid-template-columns:repeat(3,1fr);overflow:hidden;box-shadow:0 6px 18px rgba(0,0,0,.4)}
.spread--outside{top:8px}
.spread--inside{top:456px}
.panel{position:relative;overflow:hidden}
.panel--grey{background:var(--panel-grey)}
.panel--blue{background:var(--brand-blue);color:var(--white)}
.display{font-family:"Lilita One",sans-serif;color:var(--brand-blue);text-transform:uppercase;line-height:.95}
.body-copy{font-size:7.3px;line-height:1.32;text-align:justify}
.body-copy p{margin-bottom:7px}

/* outside */
.collections-title{text-align:center;font-size:16px;margin-top:38px}
.product-grid{display:grid;grid-template-columns:repeat(3,44px);gap:12px 16px;justify-content:center;margin-top:14px}
.product-shot{width:44px;height:44px;border-radius:50%;border:2px solid #fff;box-shadow:0 0 0 1px #c9cdd2;background:linear-gradient(135deg,#c8d6e6,#5d8cbf)}
.product-shot:nth-child(3n){background:linear-gradient(135deg,#e8c9c4,#3d6fa8)}
.product-shot:nth-child(4n){background:linear-gradient(135deg,#dfe6ea,#2f3d4c)}
.for-more{text-align:center;position:absolute;left:0;right:0;bottom:36px;font-size:15px}
.web-link{position:absolute;left:0;right:0;bottom:20px;text-align:center;font-weight:700;font-size:13px;color:var(--ink)}
.intro-copy{padding:40px 28px 0 28px}
.intro-copy .q{text-align:left}
.brand-foot{position:absolute;left:0;bottom:0;width:100%;height:100px}
.brand-foot__lockup{position:absolute;left:38px;bottom:30px;display:flex;align-items:center;gap:7px}
.brand-mark{width:34px;height:34px;border-radius:50%;border:2px solid var(--brand-blue)}
.brand-foot__name{font-family:"Lilita One",sans-serif;color:var(--brand-blue);font-size:12px;line-height:1.05}
.cover{text-align:center}
.cover__thirty{font-size:78px;margin-top:40px;letter-spacing:-2px}
.cover__years{font-size:17px;letter-spacing:9px;margin-top:-4px}
.cover__excellence{font-size:15px;letter-spacing:1px;margin-top:2px}
.cover__seal{width:104px;height:104px;border-radius:50%;border:3px solid var(--brand-blue);margin:24px auto 0;display:flex;align-items:center;justify-content:center}
.cover__seal span{font-family:"Lilita One",sans-serif;color:var(--brand-blue);font-size:12px;line-height:1.1;width:80px}
.cover__tagline{font-size:7px;font-weight:700;margin-top:10px}
.cover__web{font-family:"Noto Serif",serif;color:var(--brand-blue);font-size:13px}
.cover__address{position:absolute;left:14px;right:14px;bottom:16px;border-top:1px solid #9aa3ad;padding-top:8px;font-size:6.8px;line-height:1.4;color:#333}

/* inside */
.about-copy{padding:36px 0 0 22px;width:130px;font-size:7.3px;line-height:1.33;text-align:left}
.about-copy p{margin-bottom:6px}
.goals-circle{position:absolute;left:113px;top:49px;width:186px;height:186px;border-radius:50%;background:var(--accent-orange);border:4px solid var(--deep-blue);display:flex;flex-direction:column;justify-content:center;align-items:center;gap:7px;z-index:2;text-align:center}
.goals-circle .display{font-size:13px;color:var(--deep-blue);width:150px}
.goals-circle hr{width:140px;border:0;border-top:1px solid var(--deep-blue)}
.services-box{position:absolute;left:20px;top:272px;width:164px;height:138px;border:1px dashed rgba(255,255,255,.8);border-radius:8px;padding:16px 10px 0;text-align:center;font-style:italic;font-weight:600;font-size:7px;line-height:1.55}
.services-box__label{position:absolute;top:-8px;left:26px;right:26px;background:#123d6a;font-style:normal;font-weight:700;font-size:7.5px;padding:2px 0}
.services-box hr{border:0;border-top:1px solid rgba(255,255,255,.6);margin:6px 0}
.uses-title{position:absolute;right:14px;top:40px;text-align:right;font-size:15px}
.use-item{position:absolute;font-family:"Lilita One",sans-serif;font-size:9px;color:var(--ink);display:flex;align-items:center;gap:3px;line-height:.95;text-transform:uppercase}
.num{width:14px;height:14px;border-radius:50%;background:var(--accent-orange);border:1px solid var(--ink);font-size:8px;display:flex;align-items:center;justify-content:center;flex:none}
.client-circle{position:absolute;left:120px;top:256px;width:136px;height:136px;border-radius:50%;border:3px solid var(--ink);background:linear-gradient(160deg,#ffffff,#d8e2ea)}
.gift-box{position:absolute;left:42px;top:42px;width:122px;height:244px;background:#fff;border:2px solid var(--accent-orange);border-radius:6px;color:var(--ink);font-size:7px;line-height:1.36;text-align:center;padding:14px 10px}
.social-square{position:absolute;left:89px;top:333px;width:30px;height:30px;background:#2d5aa3;border-radius:3px;border:2px solid #fff}
.find-us{position:absolute;left:0;right:0;top:371px;text-align:center;font-size:7.3px;line-height:1.4}
</style>
</head>
<body>

<section class="spread spread--outside">
  <div class="panel panel--grey">
    <h2 class="display collections-title">Product<br>Collections</h2>
    <div class="product-grid">
      <div class="product-shot" role="img" aria-label="Photo of printed bandanas"></div>
      <div class="product-shot" role="img" aria-label="Photo of water bottles"></div>
      <div class="product-shot" role="img" aria-label="Photo of lunch cooler bag"></div>
      <div class="product-shot" role="img" aria-label="Photo of sport bottles"></div>
      <div class="product-shot" role="img" aria-label="Photo of table cover and tumbler"></div>
      <div class="product-shot" role="img" aria-label="Photo of embroidered cap"></div>
      <div class="product-shot" role="img" aria-label="Photo of backpack"></div>
      <div class="product-shot" role="img" aria-label="Photo of desk accessories"></div>
      <div class="product-shot" role="img" aria-label="Photo of flying disc"></div>
      <div class="product-shot" role="img" aria-label="Photo of lanyard"></div>
      <div class="product-shot" role="img" aria-label="Photo of power bank"></div>
      <div class="product-shot" role="img" aria-label="Photo of printed cards"></div>
      <div class="product-shot" role="img" aria-label="Photo of sanitizer bottle"></div>
      <div class="product-shot" role="img" aria-label="Photo of armband phone holder"></div>
      <div class="product-shot" role="img" aria-label="Photo of activity book"></div>
    </div>
    <div class="display for-more">For more...</div>
    <div class="web-link">www.keepnov.com</div>
  </div>

  <div class="panel panel--blue">
    <div class="body-copy intro-copy">
      <p>The internet is great for finding you the cheapest product. If your intention is promote yourself by the cheapest means possible continue using the internet. If you are interested in maximizing your advertising budget by finding the best possible products to meet your intended advertising market, the please call or email Keepsakes &amp; Novelties.</p>
      <p class="q">What sets us apart from our competition?</p>
      <p>In-House production capability-direct from our facility to yours- we reduce cost, and turn around time without sacrificing quality.</p>
      <p>Industry Experience-for over 35 years we've been serving our customer with the finest promotional marketing service. We've got the experience to assist you in selecting the proper promotional products.</p>
      <p>Custom Design and Manufacturing- need a custom, never before seen promotional product. Let our design team create the perfect product for your organization.</p>
    </div>
    <svg class="brand-foot" viewBox="0 0 207 100" preserveAspectRatio="none">
      <path d="M0 40 Q103 -8 207 40 L207 100 L0 100 Z" fill="#ffffff"/>
    </svg>
    <div class="brand-foot__lockup">
      <div class="brand-mark"></div>
      <div class="brand-foot__name">Keepsakes &amp;<br>Novelties<br>Products &amp; Apparel</div>
    </div>
  </div>

  <div class="panel panel--grey cover">
    <div class="display cover__thirty">30</div>
    <div class="display cover__years">Years</div>
    <div class="display cover__excellence">Excellence</div>
    <div class="cover__seal"><span>Keepsakes &amp; Novelties</span></div>
    <div class="cover__tagline">Good Products From Good People</div>
    <div class="cover__web">www.keepnov.com</div>
    <div class="cover__address">KEEPSAKES &amp; NOVELTIES<br>2045 Maple Ave: Unit 310 Haddon Falls NJ 08100<br>Phone: 555-310-2245 &bull; Fax: 555-310-2246</div>
  </div>
</section>

<section class="spread spread--inside">
  <div class="panel panel--blue">
    <div class="about-copy">
      <p>Founded in 1983, Keepsakes &amp; Novelties has been providing its customers with promotional product service excellence. International corporations, multigenerational family businesses, government agencies, local schools, and small businesses have all trusted Keepsakes &amp; Novelties to provide guidance, reliability and service excellence with regards to their promotional marketing needs.</p>
      <p>SDVOB - Service Disabled Veteran Owned Business</p>
    </div>
    <div class="services-box">
      <div class="services-box__label">IN-HOUSE SERVICES:</div>
      Promotional Product Selection and Delivery / Screen Printing / Embroidery / Engraving / Digital Print / Fulfillment / Global Sourcing/
      <hr>
      Would like pictures of automatic screen printing press, 12 head embroidery machine, various pictures of promotional products
    </div>
  </div>

  <div class="panel panel--grey">
    <h2 class="display uses-title">Top uses for<br>promotional<br>products:</h2>
    <div class="use-item" style="left:104px;top:84px"><span class="num">1</span>Brand<br>Awareness</div>
    <div class="use-item" style="left:96px;top:118px"><span class="num">2</span>Tradeshows</div>
    <div class="use-item" style="left:110px;top:139px;text-align:right">New customer /<br>account<br>generation<span class="num">3</span></div>
    <div class="use-item" style="left:96px;top:174px"><span class="num">4</span>Dealer /<br>distributor<br>programs</div>
    <div class="use-item" style="left:78px;top:218px"><span class="num">5</span>Public relation</div>
    <div class="use-item" style="left:24px;top:240px">Executive gifts<span class="num">6</span></div>
    <div class="use-item" style="left:32px;top:268px"><span class="num">7</span>Not-for-profit<br>programs</div>
    <div class="use-item" style="left:14px;top:300px;text-align:right">Product /service<br>introduction<span class="num">8</span></div>
    <div class="use-item" style="left:28px;top:338px">Employee<br>excellent<br>recognition<span class="num">9</span></div>
    <div class="use-item" style="left:48px;top:380px"><span class="num">10</span>Customer<br>referrals</div>
    <div class="client-circle" role="img" aria-label="Photo of branded client decals and stickers"></div>
  </div>

  <div class="panel panel--blue">
    <svg style="position:absolute;left:84px;top:12px" width="40" height="30" viewBox="0 0 40 30" aria-hidden="true">
      <path d="M20 24 C10 4 2 10 6 18 C9 23 16 24 20 24 C24 24 31 23 34 18 C38 10 30 4 20 24 Z" fill="none" stroke="#f7b244" stroke-width="3"/>
      <path d="M20 24 L12 30 M20 24 L28 30" stroke="#f7b244" stroke-width="3"/>
    </svg>
    <div class="gift-box">Gifts That Keep On Giving 58% of respondents keep a promotional product anywhere from one year to more than four years. Even if the recipient uses the item only once per week, that's a minimum of 52 impressions made over the course of a year with the possibility of more than 208 during a five-year window. Source: PRC Study: Effectiveness of Promotional Products As An Advertising Medium</div>
    <div class="social-square"></div>
    <div class="find-us">Find us on the web at:<br>www.keepnov.com<br>Social: @keepnov</div>
  </div>
</section>

</body>
</html>
```